Business Cards - Bluegum Haven

Design modern funky business card for disability service. Template required for name - position - contact number and email address

would like an area on the back or front for QR code that creates persons contact details in phone

```html
<!DOCTYPE html>
<html lang="en">
<head>
<meta charset="utf-8">
<title>Bluegum Haven – Business Cards</title>
<link rel="stylesheet" href="https://fonts.googleapis.com/css2?family=Arimo:wght@400;700&family=Montserrat:wght@800&display=swap">
<style>
  :root {
    --stage: #e4e3e1;
    --card: #2f2f2f;
    --card-deep: #1b1b1b;
    --emboss-light: #8c8c8c;
    --ink-white: #ffffff;
    --ink-soft: #e8e8e8;
    --rule: #cfcfcf;
    --qr-ground: #f4f4f4;
    --accent-pink: #e8178e;
    --accent-violet: #7b22e6;
    --accent-indigo: #2a0fb3;
  }
  * { box-sizing: border-box; margin: 0; padding: 0; }
  html, body {
    width: 1200px; height: 801px; overflow: hidden;
    background: var(--stage);
  }
  .sheet {
    position: relative; width: 1200px; height: 801px;
    display: flex; align-items: center; justify-content: center; gap: 40px;
  }
  .card {
    position: relative; width: 540px; height: 309px;
    background: var(--card); overflow: hidden;
    box-shadow: 0 14px 30px rgba(0,0,0,0.22);
  }
  .card::after {
    content: ""; position: absolute; left: 0; right: 0; bottom: 0; height: 5px;
    background: linear-gradient(90deg, var(--accent-indigo), var(--accent-violet) 50%, var(--accent-pink));
  }

  /* front */
  .brand {
    position: absolute; left: 30px; top: 0; bottom: 0; width: 232px;
    display: flex; flex-direction: column; justify-content: center; align-items: flex-start; gap: 12px;
    padding-top: 30px;
  }
  .brand-dot {
    width: 56px; height: 56px; border-radius: 50%;
    background: var(--accent-violet);
  }
  .brand-name {
    font-family: "Montserrat", sans-serif; font-weight: 800;
    color: var(--ink-white); font-size: 26px; line-height: 1.05; letter-spacing: -0.5px;
    white-space: nowrap;
  }
  .divider {
    position: absolute; left: 272px; top: 42px; width: 1px; height: 225px;
    background: var(--rule);
  }
  .contact {
    position: absolute; left: 296px; top: 50px; right: 20px;
    font-family: "Arimo", sans-serif; color: var(--ink-soft);
  }
  .contact-name { color: var(--accent-pink); font-weight: 700; font-size: 21px; line-height: 1.1; }
  .contact-role { font-size: 14px; margin-top: 3px; }
  .contact-address { font-size: 14px; line-height: 1.3; margin-top: 16px; }
  .contact-list { list-style: none; margin-top: 18px; }
  .contact-list li {
    display: flex; align-items: center; gap: 9px;
    font-size: 14px; line-height: 1; margin-bottom: 10px;
  }
  .contact-list svg { width: 14px; height: 14px; flex: none; }

  /* back */
  .pattern-field {
    position: absolute; inset: 0;
    background: linear-gradient(220deg, var(--emboss-light) 0%, #5a5a5a 35%, var(--card) 60%, var(--card-deep) 100%);
  }
  .back-brand {
    position: absolute; right: 60px; top: 168px;
    display: flex; align-items: center; gap: 14px;
  }
  .back-brand .brand-dot { width: 54px; height: 54px; }
  .back-brand .brand-name { font-size: 28px; }
  .qr-area {
    position: absolute; left: 34px; bottom: 40px;
    width: 96px; height: 96px; border-radius: 6px;
    background: var(--qr-ground);
    border: 3px solid var(--accent-violet);
  }
</style>
</head>
<body>
<main class="sheet">
  <section class="card card-front" aria-label="Card front">
    <div class="brand">
      <span class="brand-dot"></span>
      <span class="brand-name">Bluegum Haven</span>
    </div>
    <div class="divider"></div>
    <div class="contact">
      <p class="contact-name">Daniel Whitford</p>
      <p class="contact-role">Manager</p>
      <p class="contact-address">Your address, city<br>state, ZIP 0000</p>
      <ul class="contact-list">
        <li>
          <svg viewBox="0 0 16 16" aria-hidden="true"><path fill="var(--accent-pink)" d="M3.6 1.5l2.3 2.8-1.4 1.7c.9 2 2.5 3.6 4.5 4.5l1.7-1.4 2.8 2.3-1.3 2.3C7 13.5 2.5 9 1.3 2.8z"/></svg>
          555-318-0274
        </li>
        <li>
          <svg viewBox="0 0 16 16" aria-hidden="true"><rect x="1" y="3" width="14" height="10" fill="var(--accent-pink)"/><path d="M1 3l7 6 7-6" fill="none" stroke="var(--card)" stroke-width="1.3"/></svg>
          hello@bluegumhaven.org
        </li>
        <li>
          <svg viewBox="0 0 16 16" aria-hidden="true"><circle cx="8" cy="8" r="7" fill="var(--accent-pink)"/><path d="M1 8h14M8 1c-3 3.5-3 10.5 0 14M8 1c3 3.5 3 10.5 0 14" fill="none" stroke="var(--card)" stroke-width="1"/></svg>
          www.bluegumhaven.org
        </li>
      </ul>
    </div>
  </section>

  <section class="card card-back" aria-label="Card back">
    <div class="pattern-field" role="img" aria-label="Embossed repeating brand pattern fading from black to grey"></div>
    <div class="qr-area" role="img" aria-label="Space reserved for a QR code that saves the holder's contact details"></div>
    <div class="back-brand">
      <span class="brand-dot"></span>
      <span class="brand-name">Bluegum<br>Haven</span>
    </div>
  </section>
</main>
</body>
</html>
```